US Recruiting Firm Needs Dynamic Tri-Fold Brochure

Need tri-fold professional brochure for HR recruiting and consulting firm based in the US.

Target Market(s)

Clients seeking administrative and human resources talent

Industry/Entity Type

Recruitment

Font styles to use
Sans Serif

Requirements
Should not have
• No weird shapes
• No heavy geometric shapes -- I prefer curvy lines
• Not a dark brochure

```html
<!DOCTYPE html>
<html lang="en">
<head>
<meta charset="utf-8">
<title>Piedmont Talent Partners – Tri-Fold Brochure</title>
<link rel="stylesheet" href="https://fonts.googleapis.com/css2?family=Roboto:wght@400;500;700&family=Roboto+Condensed:wght@400;700&family=Roboto+Slab:wght@400;600&family=Oswald:wght@500;600&display=swap">
<style>
  :root{
    --navy:#17456a;
    --navy-deep:#123a5a;
    --orange:#f26a1b;
    --lime:#b8d432;
    --magenta:#c0267f;
    --ink:#4f5358;
    --paper:#ffffff;
    --backdrop:#8b8b8b;
  }
  *{box-sizing:border-box;margin:0;padding:0}
  html,body{width:1200px;height:1200px;overflow:hidden}
  body{background:var(--backdrop);font-family:"Roboto",sans-serif;position:relative}

  .brochure{position:absolute;left:45px;top:170px;width:1110px;height:860px;display:flex;box-shadow:0 18px 40px rgba(0,0,0,.25)}
  .panel{width:370px;height:100%;position:relative;overflow:hidden}

  /* Positions panel */
  .panel--positions{background:var(--paper);padding:30px 28px 20px 30px}
  .positions__intro{font-family:"Roboto Condensed",sans-serif;color:var(--magenta);font-size:16px;line-height:1.2;text-align:justify;margin-bottom:20px}
  .check-list{list-style:none}
  .positions__list li{display:flex;align-items:center;gap:12px;height:35.5px;font-family:"Roboto Condensed",sans-serif;font-size:15px;color:var(--ink)}
  .tick{width:18px;height:18px;flex:none}
  .tick--navy{color:var(--navy)}
  .tick--white{color:#fff}

  /* Services panel */
  .panel--services{background:linear-gradient(180deg,var(--navy) 0%,var(--navy-deep) 100%);padding:34px 26px 20px 28px;color:#fff}
  .services__intro{color:var(--orange);font-size:17px;line-height:1.2;text-align:justify;margin-bottom:20px}
  .services__list li{display:flex;align-items:center;gap:14px;height:36px;font-size:14.5px}
  .contact{margin-top:40px;text-align:center;font-size:13px;line-height:1.45}
  .brand{display:inline-flex;align-items:center;gap:8px;font-family:"Roboto Slab",serif;font-weight:600;font-size:15px;letter-spacing:.5px;text-transform:uppercase;color:#fff;margin-bottom:18px}
  .brand__dot{width:22px;height:22px;border-radius:50%;background:#fff;flex:none}
  .contact__cta{color:var(--orange);font-weight:700}
  .contact__item{margin-top:10px;display:flex;flex-direction:column;align-items:center;gap:3px}
  .contact__icon{width:20px;height:20px}

  /* Cover panel */
  .panel--cover{background:var(--navy)}
  .cover__top{position:absolute;left:0;top:0;width:100%;height:190px;background:var(--paper);display:flex;align-items:center;justify-content:center}
  .cover__top .brand{color:var(--navy);font-size:16px;margin:0}
  .cover__top .brand__dot{background:var(--orange)}
  .cover__photo{position:absolute;left:0;top:190px;width:100%;height:380px;background:linear-gradient(160deg,#f2f4f6 0%,#c9ced4 45%,#5c6670 75%,#eef0f2 100%);border-radius:0 0 50% 50% / 0 0 48% 48%}
  .cover__headline{position:absolute;left:0;top:610px;width:100%;text-align:center;line-height:1.15}
  .headline__lead{display:block;font-family:"Roboto Slab",serif;color:var(--lime);font-size:28px}
  .headline__body{display:block;color:#fff;font-size:27px}
  .headline__accent{display:block;font-family:"Oswald",sans-serif;font-weight:600;color:var(--orange);font-size:31px;letter-spacing:.5px}
  .cover__web{position:absolute;left:20px;right:20px;bottom:30px;display:flex;align-items:center;gap:12px;color:#fff;font-size:12px;letter-spacing:4px;white-space:nowrap}
  .cover__web::before,.cover__web::after{content:"";flex:1;height:1px;background:rgba(255,255,255,.8)}
</style>
</head>
<body>
<svg width="0" height="0" style="position:absolute" aria-hidden="true">
  <symbol id="tick" viewBox="0 0 20 20">
    <circle cx="10" cy="10" r="8.5" fill="none" stroke="currentColor" stroke-width="1.8"/>
    <path d="M5.8 10.3l2.9 2.9 5.5-6" fill="none" stroke="currentColor" stroke-width="2.2" stroke-linecap="round" stroke-linejoin="round"/>
  </symbol>
</svg>

<main class="brochure">
  <section class="panel panel--positions">
    <p class="positions__intro">We offer stellar HR talent from entry to executive level. Positions that we fill include:</p>
    <ul class="check-list positions__list">
      <li><svg class="tick tick--navy"><use href="#tick"/></svg>HR Assistant</li>
      <li><svg class="tick tick--navy"><use href="#tick"/></svg>HR Coordinator</li>
      <li><svg class="tick tick--navy"><use href="#tick"/></svg>HR Specialist</li>
      <li><svg class="tick tick--navy"><use href="#tick"/></svg>HR Generalist</li>
      <li><svg class="tick tick--navy"><use href="#tick"/></svg>HR Consultant</li>
      <li><svg class="tick tick--navy"><use href="#tick"/></svg>HR Manager</li>
      <li><svg class="tick tick--navy"><use href="#tick"/></svg>Employee Relations Specialist</li>
      <li><svg class="tick tick--navy"><use href="#tick"/></svg>Employee Relations Manager</li>
      <li><svg class="tick tick--navy"><use href="#tick"/></svg>Talent Acquisition Consultant</li>
      <li><svg class="tick tick--navy"><use href="#tick"/></svg>Talent Acquisition Specialist</li>
      <li><svg class="tick tick--navy"><use href="#tick"/></svg>Recruiter</li>
      <li><svg class="tick tick--navy"><use href="#tick"/></svg>Recruiter/HR Generalist</li>
      <li><svg class="tick tick--navy"><use href="#tick"/></svg>Benefits Coordinator</li>
      <li><svg class="tick tick--navy"><use href="#tick"/></svg>Benefits Specialist</li>
      <li><svg class="tick tick--navy"><use href="#tick"/></svg>Compensation Specialist</li>
      <li><svg class="tick tick--navy"><use href="#tick"/></svg>Compensation Manager</li>
      <li><svg class="tick tick--navy"><use href="#tick"/></svg>Training Specialist</li>
      <li><svg class="tick tick--navy"><use href="#tick"/></svg>Learning &amp; Development Consultant</li>
      <li><svg class="tick tick--navy"><use href="#tick"/></svg>Diversity and Inclusion Consultant</li>
    </ul>
  </section>

  <section class="panel panel--services">
    <p class="services__intro">We provide customized recruiting and consulting services.</p>
    <ul class="check-list services__list">
      <li><svg class="tick tick--white"><use href="#tick"/></svg>Working with hiring managers on requisitions</li>
      <li><svg class="tick tick--white"><use href="#tick"/></svg>Position &amp; Candidate Profiling</li>
      <li><svg class="tick tick--white"><use href="#tick"/></svg>Sourcing resumes</li>
      <li><svg class="tick tick--white"><use href="#tick"/></svg>Writing and placing job postings</li>
      <li><svg class="tick tick--white"><use href="#tick"/></svg>Screening and interviewing candidates</li>
      <li><svg class="tick tick--white"><use href="#tick"/></svg>Shortlisting Candidates</li>
      <li><svg class="tick tick--white"><use href="#tick"/></svg>Candidate Assessment</li>
      <li><svg class="tick tick--white"><use href="#tick"/></svg>Coordinating Interviews &amp; Debriefing</li>
      <li><svg class="tick tick--white"><use href="#tick"/></svg>Candidate Dispositioning &amp; Updates</li>
      <li><svg class="tick tick--white"><use href="#tick"/></svg>Applicant Tracking</li>
      <li><svg class="tick tick--white"><use href="#tick"/></svg>Job Offers &amp; Salary Negotiation</li>
      <li><svg class="tick tick--white"><use href="#tick"/></svg>Start Date Coordination &amp; Offer Letter</li>
      <li><svg class="tick tick--white"><use href="#tick"/></svg>Onboarding Process / New Hire Paperwork</li>
    </ul>

    <div class="contact">
      <div class="brand"><span class="brand__dot"></span>Piedmont Talent Partners</div>
      <p>To learn more and request</p>
      <p class="contact__cta">A FREE CONSULTATION</p>
      <p>contact us today</p>
      <div class="contact__item">
        <svg class="contact__icon" viewBox="0 0 20 20" aria-hidden="true"><path d="M6 2h4l1 4-2.2 1.4a10 10 0 0 0 3.8 3.8L14 9l4 1v4c0 1-1 2-2 2A14 14 0 0 1 4 4c0-1 1-2 2-2z" fill="var(--lime)"/></svg>
        <span>555-014-2290</span>
      </div>
      <div class="contact__item">
        <svg class="contact__icon" viewBox="0 0 20 20" aria-hidden="true"><rect x="2" y="5" width="16" height="11" rx="1.5" fill="none" stroke="var(--lime)" stroke-width="1.8"/><path d="M2.5 6l7.5 6 7.5-6" fill="none" stroke="var(--lime)" stroke-width="1.8"/></svg>
        <span>hello@piedmonttalent.com</span>
      </div>
      <div class="contact__item">
        <svg class="contact__icon" viewBox="0 0 20 20" aria-hidden="true"><g fill="none" stroke="var(--lime)" stroke-width="1.6"><circle cx="10" cy="10" r="8"/><ellipse cx="10" cy="10" rx="3.5" ry="8"/><path d="M2 10h16M3.5 6h13M3.5 14h13"/></g></svg>
        <span>www.piedmonttalent.com</span>
      </div>
    </div>
  </section>

  <section class="panel panel--cover">
    <div class="cover__top">
      <div class="brand"><span class="brand__dot"></span>Piedmont Talent Partners</div>
    </div>
    <div class="cover__photo" role="img" aria-label="Photo of smiling business professionals shaking hands across a meeting table"></div>
    <h1 class="cover__headline">
      <span class="headline__lead">Specializing in</span>
      <span class="headline__body">administrative,</span>
      <span class="headline__accent">PROFESSIONAL AND</span>
      <span class="headline__body">executive HR Talent</span>
    </h1>
    <p class="cover__web">www.piedmonttalent.com</p>
  </section>
</main>
</body>
</html>
```